Journal Cover Design Project

The Worldwide Review of Rising Trade Systems is a professional journal which aims to provide an international platform for publication of original research on the emerging economies.
The journal is published three times a year and available by subscription. Currently, the cover design is the same for each issue. We are looking to redesign the cover (and interior) of our journal and would like a design that would allow us to change the color scheme for each issue or volume while maintaining a consistent design scheme.
Our design preference is simple and modern with good use of color. Many of our past publications have used abstract maps/globes but we are open to new ideas. We would need a creative way to include text on the cover, possibly a way to present the article titles or main topics for each issue. For example, we like the use of color and the general design in this image: http://www.pixmoravo.example/photos/drawdreamhope/5182640913/lightbox/
Below is a link to our most recent issue of the journal. You can see an example of the article titles, structure, etc. The website also shows the current cover of the journal (but we do not want the new design to be based off of the current one):
http://rts.quilberpress.example/content/4/2.toc

```html
<!DOCTYPE html>
<html lang="en">
<head>
<meta charset="utf-8">
<title>Worldwide Review of Rising Trade Systems — Volume 5, Issue 1</title>
<link rel="stylesheet" href="https://fonts.googleapis.com/css2?family=Roboto+Condensed:wght@400;700&display=swap">
<style>
  :root {
    --page: #ffffff;
    --night: #0f1821;
    --sky: #bfe2f5;
    --sky-deep: #9cc6df;
    --signal: #e8352a;
    --ember: #ec6a4c;
    --ink: #101417;
    --paper: #ffffff;
  }
  * { margin: 0; padding: 0; box-sizing: border-box; }
  html, body {
    width: 1001px; height: 1200px; overflow: hidden;
    background: var(--page);
    font-family: "Roboto Condensed", "Arial Narrow", sans-serif;
  }
  .cover {
    position: absolute; left: 68px; top: 24px;
    width: 868px; height: 1134px;
    background: var(--sky);
    overflow: hidden;
    box-shadow: 0 2px 6px rgba(0,0,0,.18);
  }
  .cover__night {
    position: absolute; left: 0; top: 0; width: 100%; height: 456px;
    background: var(--night);
  }
  .cover__mesh {
    position: absolute; left: 0; top: 0; width: 100%; height: 250px;
    background: linear-gradient(180deg, rgba(255,255,255,.16), rgba(255,255,255,0));
  }
  .cover__tiles-top {
    position: absolute; left: 0; top: 110px; width: 560px; height: 346px;
    background: linear-gradient(90deg, rgba(60,20,18,.7), rgba(60,20,18,.05));
  }
  .cover__tiles {
    position: absolute; left: 0; top: 470px; width: 440px; height: 600px;
    background: linear-gradient(160deg, var(--ember) 0%, #c5584a 45%, rgba(236,106,76,.35) 80%, rgba(236,106,76,0) 100%);
  }
  .cover__tower {
    position: absolute; left: 448px; top: 456px; width: 420px; height: 660px;
    background: linear-gradient(180deg, var(--sky) 0%, var(--sky-deep) 60%, #8fb8d2 100%);
  }
  .cover__base {
    position: absolute; left: 0; bottom: 0; width: 100%; height: 20px;
    background: var(--night);
  }
  .issue-badge {
    position: absolute; left: 719px; top: 0; width: 89px; height: 148px;
    background: var(--signal); color: var(--paper);
    font-weight: 700; text-align: center;
  }
  .issue-badge__volume {
    position: absolute; left: 4px; top: 14px;
    writing-mode: vertical-rl; transform: rotate(180deg);
    font-size: 17px; letter-spacing: .5px;
  }
  .issue-badge__number { position: absolute; left: 26px; top: 4px; font-size: 92px; line-height: 1; }
  .issue-badge__issue { position: absolute; left: 0; right: 0; top: 116px; font-size: 19px; }
  .masthead {
    position: absolute; right: 60px; top: 300px; text-align: right; font-weight: 700;
  }
  .masthead__title { color: var(--signal); font-size: 72px; line-height: 1; letter-spacing: -.5px; }
  .masthead__subtitle { color: var(--paper); font-size: 47px; line-height: 1.15; margin-top: 6px; }
  .contents {
    position: absolute; right: 28px; top: 496px; text-align: right; color: var(--ink);
  }
  .contents__item { margin-bottom: 20px; }
  .contents__heading { font-weight: 700; font-size: 32px; line-height: 1.12; }
  .contents__sub { font-weight: 700; font-size: 16.5px; line-height: 1.3; }
  .issue-date {
    position: absolute; left: 58px; top: 1040px;
    font-weight: 700; font-size: 27px; color: var(--ink);
  }
  .partner {
    position: absolute; top: 1040px; display: flex; align-items: center; gap: 6px;
    font-weight: 700; font-size: 15px; line-height: 1.05; color: var(--ink);
  }
  .partner--circle { left: 650px; }
  .partner--press { left: 778px; }
  .partner__square { width: 22px; height: 22px; background: var(--ink); }
  .partner__circle { width: 26px; height: 26px; border-radius: 50%; background: var(--ink); }
</style>
</head>
<body>
  <main class="cover">
    <div class="cover__night"></div>
    <div class="cover__mesh" role="img" aria-label="White wire globe mesh curving across the top"></div>
    <div class="cover__tiles-top" role="img" aria-label="Faint dark square tiles over the night band"></div>
    <div class="cover__tower" role="img" aria-label="Pale blue photo of a high-rise office tower"></div>
    <div class="cover__tiles" role="img" aria-label="Grid of orange and black square tiles fading out to the right"></div>
    <div class="cover__base"></div>

    <div class="issue-badge">
      <span class="issue-badge__volume">VOLUME</span>
      <span class="issue-badge__number">5</span>
      <span class="issue-badge__issue">ISSUE 1</span>
    </div>

    <header class="masthead">
      <h1 class="masthead__title">Worldwide Review</h1>
      <p class="masthead__subtitle">of Rising Trade Systems</p>
    </header>

    <section class="contents">
      <article class="contents__item">
        <h2 class="contents__heading">Construction<br>and Analysis</h2>
        <p class="contents__sub">of a Global GDP Growth<br>Model for 185 Countries<br>through 2050</p>
      </article>
      <article class="contents__item">
        <h2 class="contents__heading">New Directions</h2>
        <p class="contents__sub">for Water Management<br>in Indian Agriculture</p>
      </article>
      <article class="contents__item">
        <h2 class="contents__heading">A New Vision<br>for Mexico 2042</h2>
        <p class="contents__sub">Achieving Prosperity for All</p>
      </article>
      <article class="contents__item">
        <h2 class="contents__heading">India 2039</h2>
        <p class="contents__sub">Transforming Agriculture:<br>Productivity, Markets,<br>and Institutions</p>
      </article>
    </section>

    <p class="issue-date">08/2012</p>

    <div class="partner partner--circle">
      <span class="partner__square"></span>
      <span>Rising<br>Markets<br>Circle</span>
    </div>
    <div class="partner partner--press">
      <span class="partner__circle"></span>
      <span>Quilber<br>Press</span>
    </div>
  </main>
</body>
</html>
```